Quiet Ledgers and the Erosion of Healing: What Every Patient Should Hear

bookvane leafpad pub and print on demand. Here are similar books with terrible covers: https://www.bookvane.example/Silent-Remedies-Hidden-Trade-Wellness/dp/3920417755
https://www.bookvane.example/Anxious-Ward-Dosage-Overtended-Nation/dp/2918463310
https://www.bookvane.example/Grim-Tonics-Firms-Deceive-Clients/dp/2954189903
https://www.bookvane.example/s/?q=tonicfall&src=srch-4410
https://www.bookvane.example/Overfilled-Nation-Pledge-Modern-Healing/dp/0172455872
https://www.bookvane.example/Tethered-Calling-Remedy-Inquiries-Letters/dp/0853663206
https://www.bookvane.example/dp/X77R5K3H8Q/ref=dp-reader-redirect
https://www.bookvane.example/Sultans-Fresh-Tonics-Bursting-Moodlifter/dp/0576133117
https://www.bookvane.example/Lethal-Alienism-Arranged-Refusal-Varnholt-ebook/dp/X925TP8JKW

Help! you can do better than this!

Target Market(s)

medical readers science readers

Colors

Designer to choose colors to be used in the design.

Requirements
Must have
• great eye catching cover here is excerpt
• As my insight grew, I discovered patient after patient who was broken on the torture-wheel of our therapies, their lives ruined by toxic drugs or surgery. I saw men with back pain which likely would have been self-limited turned into struggling opioid addicts by our promiscuous prescribing culture. Some had surgery supported by no more science than a bar stabbing. I saw people taking ten or more prescriptions. I saw depression and intellectual decline with statin and beta blocker combinations. I saw irreversible brain damage from psychiatric drugs. I saw a lot more.
• As I learned, I felt obliged to share my discoveries, so I began to write. I will take you through my journey step by step. I use quotes, links, and explanatory footnotes liberally to make authentication easy. As you start to grasp the tragedy, you will realize why I cannot sugar-coat or use euphemisms.
Nice to have
• reasonable dignity (no gravestones) but this is a serious subject
• it's freaking a terrible situation
• hope you can do better than the other examples

```html
<!DOCTYPE html>
<html lang="en">
<head>
<meta charset="utf-8">
<title>Quiet Ledgers and the Erosion of Healing</title>
<link rel="stylesheet" href="https://fonts.googleapis.com/css2?family=Arimo:wght@400;500&family=Josefin+Sans:wght@300&display=swap">
<style>
  :root {
    --sky-top: #2f98cc;
    --sky-bottom: #1b6e9f;
    --blood-top: #d82b2b;
    --blood-bottom: #9c1419;
    --band: #ece6d6;
    --label: #f3efe3;
    --title-red: #c4202a;
    --ink: #1c2436;
    --rule: #6f6f6f;
    --author: #ffffff;
  }
  * { margin: 0; padding: 0; box-sizing: border-box; }
  html, body { width: 800px; height: 1200px; overflow: hidden; background: #ffffff; }
  .cover {
    position: relative;
    width: 800px;
    height: 1200px;
    overflow: hidden;
    background: linear-gradient(180deg, var(--sky-top) 0%, var(--sky-bottom) 61.3%, var(--blood-top) 61.3%, var(--blood-bottom) 100%);
  }
  .tray-art {
    position: absolute;
    left: 168px;
    top: 255px;
    width: 464px;
    height: 665px;
    border-radius: 34px;
    background: linear-gradient(160deg, #fdfdfd 0%, #e9ecef 55%, #c9cdd2 100%);
    box-shadow: 0 14px 30px rgba(0,0,0,0.35);
  }
  .syringe-art {
    position: absolute;
    left: 355px;
    top: 20px;
    width: 92px;
    height: 1040px;
    transform: rotate(-9deg);
    transform-origin: 50% 50%;
    border-radius: 40px 40px 4px 4px;
    background: linear-gradient(180deg, #b9b7ad 0%, #9f9a6e 35%, #c4b24a 65%, #8d8a80 88%, #3a3a3a 100%);
    opacity: 0.85;
  }
  .title-band {
    position: absolute;
    left: 165px;
    top: 408px;
    width: 470px;
    height: 357px;
    background: var(--band);
    box-shadow: 0 6px 16px rgba(0,0,0,0.3);
  }
  .title-label {
    position: absolute;
    left: 25px;
    top: 12px;
    width: 425px;
    height: 330px;
    background: var(--label);
    display: flex;
    flex-direction: column;
    align-items: center;
    justify-content: center;
    font-family: "Arimo", Arial, sans-serif;
    text-align: center;
  }
  .title-line {
    width: 355px;
    padding: 8px 0 10px;
  }
  .title-line + .title-line { border-top: 1px solid var(--rule); }
  .title-lead { color: var(--title-red); font-size: 42px; font-weight: 400; letter-spacing: 0.5px; line-height: 1.1; }
  .title-join { color: var(--ink); font-size: 29px; line-height: 1.15; }
  .title-key { color: var(--ink); font-size: 38px; line-height: 1.15; }
  .subtitle { color: var(--ink); font-size: 22px; line-height: 1.2; }
  .author {
    position: absolute;
    left: 0;
    width: 800px;
    top: 1075px;
    text-align: center;
    font-family: "Josefin Sans", "Gill Sans", sans-serif;
    font-weight: 300;
    font-size: 50px;
    letter-spacing: 5px;
    color: var(--author);
  }
</style>
</head>
<body>
<main class="cover">
  <div class="tray-art" role="img" aria-label="White enamel medical tray holding two red-and-green capsules"></div>
  <div class="syringe-art" role="img" aria-label="Large vintage glass syringe with amber liquid lying diagonally across the tray, needle pointing down"></div>
  <section class="title-band">
    <div class="title-label">
      <h1 class="title-line title-lead">QUIET LEDGERS</h1>
      <p class="title-line title-join">and the Erosion of</p>
      <p class="title-line title-key">Healing</p>
      <p class="title-line subtitle">What Every Patient Should Hear</p>
    </div>
  </section>
  <p class="author">WARREN DELACOURT</p>
</main>
</body>
</html>
```